Pellowick bottle design

We're a small company looking for someone to help with our bottle design. We provide a sauce that will boost the flavor of packaged ramen. We're looking for a label that will stand out. I'm attaching some of the labels we like and some that I've made.

```html
<!DOCTYPE html>
<html lang="en">
<head>
<meta charset="utf-8">
<title>Pellowick Ramen Sauce Labels</title>
<link href="https://fonts.googleapis.com/css2?family=Jost:wght@500;600;700&display=swap" rel="stylesheet">
<style>
  :root {
    --backdrop: #efe9df;
    --label-light: #f1efea;
    --label-dark: #1e1517;
    --ink-dark: #1f1719;
    --ink-light: #ffffff;
    --accent-red: #e3262e;
  }
  html, body {
    margin: 0;
    padding: 0;
    width: 1200px;
    height: 800px;
    overflow: hidden;
    background: var(--backdrop);
  }
  .canvas {
    position: relative;
    width: 1200px;
    height: 800px;
    background: var(--backdrop);
  }
  .label {
    position: absolute;
    top: 90px;
    width: 162px;
    height: 620px;
    overflow: hidden;
    font-family: "Jost", "Futura", sans-serif;
    text-align: center;
  }
  .label--light { left: 384px; background: var(--label-light); color: var(--ink-dark); }
  .label--dark  { left: 664px; background: var(--label-dark);  color: var(--ink-light); }

  .brand-name {
    position: absolute;
    top: 58px;
    left: 0;
    width: 100%;
    margin: 0;
    font-size: 23px;
    font-weight: 700;
    letter-spacing: 0.04em;
    line-height: 1;
    text-transform: uppercase;
  }
  .emblem {
    position: absolute;
    top: 182px;
    left: -28px;
    width: 218px;
    height: 218px;
  }
  .product-type {
    position: absolute;
    top: 480px;
    left: 0;
    width: 100%;
    margin: 0;
    font-size: 16px;
    font-weight: 600;
    letter-spacing: 0.03em;
    line-height: 1;
    text-transform: uppercase;
  }
  .product-origin {
    position: absolute;
    top: 501px;
    left: 0;
    width: 100%;
    margin: 0;
    font-size: 13.5px;
    font-weight: 600;
    letter-spacing: 0.05em;
    line-height: 1;
    text-transform: uppercase;
  }
  .divider-dot {
    position: absolute;
    top: 550px;
    left: 76px;
    width: 10px;
    height: 10px;
    border-radius: 50%;
    background: currentColor;
  }
  .volume {
    position: absolute;
    top: 586px;
    left: 0;
    width: 100%;
    margin: 0;
    font-size: 13.5px;
    font-weight: 600;
    letter-spacing: 0.03em;
    line-height: 1;
    text-transform: uppercase;
  }
</style>
</head>
<body>
  <main class="canvas">
    <section class="label label--light">
      <h1 class="brand-name">Pellowick</h1>
      <svg class="emblem" viewBox="0 0 218 218" role="img" aria-label="Spiral noodle emblem in red and black">
        <defs>
          <radialGradient id="emblem-fill-light" cx="0.45" cy="0.5" r="0.5">
            <stop offset="0" stop-color="var(--accent-red)" style="stop-color:#e3262e"/>
            <stop offset="0.65" stop-color="#c0242b"/>
            <stop offset="0.78" stop-color="#5a3336"/>
            <stop offset="1" stop-color="#8a8584"/>
          </radialGradient>
        </defs>
        <circle cx="109" cy="109" r="109" fill="url(#emblem-fill-light)"/>
      </svg>
      <p class="product-type">Ramen Sauce</p>
      <p class="product-origin">Ohio’s Best</p>
      <span class="divider-dot"></span>
      <p class="volume">11.2 fl oz (330ml)</p>
    </section>

    <section class="label label--dark">
      <h1 class="brand-name">Pellowick</h1>
      <svg class="emblem" viewBox="0 0 218 218" role="img" aria-label="Spiral noodle emblem in red and white">
        <defs>
          <radialGradient id="emblem-fill-dark" cx="0.45" cy="0.5" r="0.5">
            <stop offset="0" stop-color="#f06a6f"/>
            <stop offset="0.65" stop-color="#e3262e"/>
            <stop offset="0.78" stop-color="#6a3437"/>
            <stop offset="1" stop-color="#8c8888"/>
          </radialGradient>
        </defs>
        <circle cx="109" cy="109" r="109" fill="url(#emblem-fill-dark)"/>
      </svg>
      <p class="product-type">Ramen Sauce</p>
      <p class="product-origin">Ohio’s Best</p>
      <span class="divider-dot"></span>
      <p class="volume">11.2 fl oz (330ml)</p>
    </section>
  </main>
</body>
</html>
```